INNOVATIVE DESIGN NEEDED FOR FINANCIAL COMPANY

INTERNATIONAL FIRM IN HONG KONG NEEDS A MODERN BUSINESS CARD DESIGN. ONE SIDE ENGLISH OTHER SIDE IN CHINESE. WE ARE OPEN TO CHANGING FONTS AND COLOR. SHOULD BE A CARD THAT IS PROFESSIONAL DEALING WITH HIGH NET WORTH CLIENTELE. BOTH SIDES OF THE CARD WILL BE THE SAME, HOWEVER, THE WORDING ON ONE SIDE WILL BE ENGLISH AND THE OTHER SIDE IN CHINESE (CAN ASSIST IN THE LETTERING - CAN PROVIDE ONCE CARD DESIGN IS ACCEPTED.

Target Market(s)

Hong Kong/CHINA

Contact Information for Business Card

ATTRACTIVE MODERN

```html
<!DOCTYPE html>
<html lang="en">
<head>
<meta charset="utf-8">
<title>Cedarline Asset Management – Business Card</title>
<link href="https://fonts.googleapis.com/css2?family=Lato:wght@700&family=Noto+Sans+TC:wght@700&family=Source+Sans+3:wght@400;600&display=swap" rel="stylesheet">
<style>
  :root {
    --brand-green: #138a66;
    --ink: #1c1c1c;
    --logo-grey: #3d3d3d;
    --paper: #ffffff;
    --backdrop: #ece8e3;
  }
  html, body {
    margin: 0;
    padding: 0;
    width: 1200px;
    height: 900px;
    overflow: hidden;
    background: var(--backdrop);
  }
  .canvas {
    position: relative;
    width: 1200px;
    height: 900px;
  }
  .card {
    position: absolute;
    width: 556px;
    height: 343px;
    box-shadow: 3px 4px 8px rgba(0,0,0,0.35);
    font-family: "Source Sans 3", "Noto Sans TC", sans-serif;
    color: var(--ink);
  }
  .card--front { left: 330px; top: 90px; background: var(--paper); }
  .card--back  { left: 330px; top: 470px; background: var(--brand-green); color: #fff; }

  .brand {
    position: absolute;
    left: 86px;
    top: 72px;
    display: flex;
    align-items: center;
    gap: 10px;
  }
  .brand__dot {
    width: 70px;
    height: 70px;
    border-radius: 50%;
    background: var(--brand-green);
    flex: none;
  }
  .card--back .brand__dot { background: #fff; }
  .brand__name {
    font-family: "Lato", "Noto Sans TC", sans-serif;
    font-weight: 700;
    color: var(--logo-grey);
    line-height: 1;
  }
  .card--back .brand__name { color: #fff; }
  .brand__name-zh {
    display: block;
    font-size: 30px;
    letter-spacing: 2px;
  }
  .brand__name-en {
    display: block;
    margin-top: 5px;
    font-size: 14px;
    letter-spacing: 1.6px;
  }

  .details {
    position: absolute;
    left: 0;
    right: 0;
    top: 170px;
    text-align: center;
  }
  .person__name {
    font-family: "Lato", sans-serif;
    font-weight: 700;
    font-size: 20px;
    color: var(--brand-green);
    line-height: 24px;
  }
  .card--back .person__name { color: #fff; }
  .person__title {
    font-size: 15px;
    line-height: 19px;
  }
  .rule {
    width: 195px;
    height: 1px;
    margin: 6px auto 7px;
    background: currentColor;
  }
  .contact {
    font-size: 15px;
    line-height: 20px;
  }
  .contact__label {
    font-weight: 600;
    color: var(--brand-green);
  }
  .card--back .contact__label { color: #fff; }
  .address {
    font-size: 15px;
    line-height: 20px;
    margin-top: 10px;
  }
</style>
</head>
<body>
<main class="canvas">

  <section class="card card--front" aria-label="Business card, light side">
    <div class="brand">
      <span class="brand__dot"></span>
      <span class="brand__name">
        <span class="brand__name-zh" lang="zh-Hant">松雅資產管理有限公司</span>
        <span class="brand__name-en">Cedarline Asset Management Ltd</span>
      </span>
    </div>
    <div class="details">
      <div class="person__name">DANIEL CARTER</div>
      <div class="person__title">Managing Director</div>
      <div class="rule"></div>
      <div class="contact"><span class="contact__label">P:</span> 044-123 456 789 | <span class="contact__label">M:</span> 044-123 456 789</div>
      <div class="contact"><span class="contact__label">E:</span> info@webname.com | <span class="contact__label">W:</span> www.websitename.com</div>
      <div class="rule"></div>
      <div class="address" style="margin-top:0">12345, Address Goes Here Country Name, 123456.</div>
    </div>
  </section>

  <section class="card card--back" aria-label="Business card, green side">
    <div class="brand">
      <span class="brand__dot"></span>
      <span class="brand__name">
        <span class="brand__name-zh" lang="zh-Hant">松雅資產管理有限公司</span>
        <span class="brand__name-en">Cedarline Asset Management Ltd</span>
      </span>
    </div>
    <div class="details">
      <div class="person__name">DANIEL CARTER</div>
      <div class="person__title">Managing Director</div>
      <div class="rule"></div>
      <div class="contact"><span class="contact__label">P:</span> 044-123 456 789 | <span class="contact__label">M:</span> 044-123 456 789</div>
      <div class="contact"><span class="contact__label">E:</span> info@webname.com | <span class="contact__label">W:</span> www.websitename.com</div>
      <div class="rule"></div>
      <div class="address" style="margin-top:0">12345, Address Goes Here Country Name, 123456.</div>
    </div>
  </section>

</main>
</body>
</html>
```